Ridgeline Outfitters Business Cards

Recently had a logo done with Artfolio and now looking for a business card to go along with it.

Target Market(s)

Ridgeline Outfitters is a weapons dealer. My market will be primarily men, hunting, shooting type.

Industry/Entity Type

Business

Contact Information for Business Card

I selected double sided, but this is not required, single or double is going to be fine. I picture the logo on one side, or perhaps just the circle which contains "RO" with the remaining info on the other side.

Font styles to use
Sans Serif

Requirements
Must have
• My name: Milo Brandt
• Title: Owner
• tel: 612-555-0187
• web: www.ridgelineoutfittersmn.example
Nice to have
• I like the concept of a black business card. I would like to keep the colors monotone, black, grey, white or red. Red is acceptable because it is in the logo. I have also seen cards that are matte black with shiny black as well, perhaps for the logo (or circle RO) part of the logo.
• I will upload a couple of the logos for use, and also an example I just found of the black on black. and some others that have a nice contrast.
Should not have
• lots of colors are not wanted.

```html
<!DOCTYPE html>
<html lang="en">
<head>
<meta charset="utf-8">
<title>Ridgeline Outfitters Business Card</title>
<link rel="stylesheet" href="https://fonts.googleapis.com/css2?family=Fira+Sans:wght@400;600;700&display=swap">
<style>
  :root {
    --page: #5a5a5a;
    --card: #1f1f21;
    --gloss: #3a3a3d;
    --gloss-light: #4a4a4e;
    --white: #ffffff;
    --red: #d0161b;
  }
  * { margin: 0; padding: 0; box-sizing: border-box; }
  html, body {
    width: 799px;
    height: 1200px;
    overflow: hidden;
    background: var(--page);
    font-family: "Fira Sans", sans-serif;
  }
  .sheet {
    position: relative;
    width: 799px;
    height: 1200px;
  }
  .card {
    position: absolute;
    left: 80px;
    width: 640px;
    height: 366px;
    background: var(--card);
    box-shadow: 0 10px 24px rgba(0,0,0,0.45);
  }
  .card--front { top: 117px; }
  .card--back { top: 717px; }

  .brand {
    position: absolute;
    display: flex;
    align-items: center;
    color: var(--gloss-light);
    font-weight: 600;
    white-space: nowrap;
  }
  .brand__ring {
    border: 3px solid var(--gloss-light);
    border-radius: 50%;
    flex: none;
  }
  .card--front .brand {
    left: 50%;
    top: 50%;
    transform: translate(-50%, -50%);
    gap: 18px;
    font-size: 30px;
  }
  .card--front .brand__ring { width: 84px; height: 84px; border-width: 6px; }

  .card--back .brand {
    right: 44px;
    top: 52px;
    gap: 12px;
    font-size: 20px;
    color: var(--gloss);
  }
  .card--back .brand__ring { width: 50px; height: 50px; border-color: var(--gloss); border-width: 4px; }

  .contact {
    position: absolute;
    left: 46px;
    top: 164px;
    color: var(--white);
  }
  .contact__name {
    font-size: 24px;
    font-weight: 700;
    letter-spacing: 0.3px;
    line-height: 1;
  }
  .contact__title {
    color: var(--red);
    font-size: 13px;
    margin-top: 2px;
    margin-bottom: 14px;
  }
  .contact__line {
    display: flex;
    align-items: center;
    gap: 8px;
    font-size: 15px;
    line-height: 1.55;
  }
  .contact__icon { width: 13px; height: 13px; fill: var(--white); flex: none; }
</style>
</head>
<body>
<main class="sheet">
  <section class="card card--front">
    <div class="brand">
      <span class="brand__ring"></span>
      <span class="brand__name">Ridgeline Outfitters</span>
    </div>
  </section>

  <section class="card card--back">
    <div class="brand">
      <span class="brand__ring"></span>
      <span class="brand__name">Ridgeline Outfitters</span>
    </div>

    <div class="contact">
      <p class="contact__name">MILO BRANDT</p>
      <p class="contact__title">Owner</p>
      <p class="contact__line">
        <svg class="contact__icon" viewBox="0 0 16 16" aria-hidden="true">
          <path d="M3.5 1.5l2.5 0 1.2 3-1.6 1.2c.8 1.8 2.4 3.4 4.2 4.2l1.2-1.6 3 1.2 0 2.5c0 .8-.7 1.5-1.5 1.5C6.7 13.5 2 8.8 2 3c0-.8.7-1.5 1.5-1.5z"/>
        </svg>
        <span>612-555-0187</span>
      </p>
      <p class="contact__line">
        <svg class="contact__icon" viewBox="0 0 16 16" aria-hidden="true">
          <path d="M8 1a7 7 0 100 14A7 7 0 008 1zm0 1.5c.9 0 1.9 1.6 2.2 4H5.8C6.1 4.1 7.1 2.5 8 2.5zM2.6 6.5h1.7c0 .5-.1 1-.1 1.5s0 1 .1 1.5H2.6A5.6 5.6 0 012.6 6.5zm3.2 3h4.4c-.3 2.4-1.3 4-2.2 4s-1.9-1.6-2.2-4zm5.9 0c.1-.5.1-1 .1-1.5s0-1-.1-1.5h1.7a5.6 5.6 0 010 3h-1.7zM5.7 8c0-.5 0-1 .1-1.5h4.4c.1.5.1 1 .1 1.5s0 1-.1 1.5H5.8C5.7 9 5.7 8.5 5.7 8z"/>
        </svg>
        <span>www.ridgelineoutfittersmn.example</span>
      </p>
    </div>
  </section>
</main>
</body>
</html>
```